依頼詳細
載内容詳細に関しては、別添のExcel資料を参照してください。

・ターゲット
BtoB
木工架装を出来る業者を探している車のリース販売会社の担当様

・カラーイメージ
木目デザインと企業カラーである紺色を使用してデザインお願いします
▼木目参考
https://www.haruki-mokuzai.jp/
▼紺参考
https://www.tmr-w.jp/

・デザイン、ムード
木を扱う仕事なので、木目を上手く使ってデザインしてほしい
▼参考

・JQについて
JQのパターン制作は不要です。
1枚目の画像でデザインお願いします

配置やデザイン等はアレンジしていただいて構いません。
また、縦に制限はありません。

レスポンシブデザインのサイトで、bootstrap4を利用しコーディングする予定になります。

デザイン幅は2000px、コンテンツの幅はbootstrap4デフォルトのの1110pxを基準としてください。
ただし、最近のデザインの流行を取りいれて、フルワイドや、1200~15000px程度の幅のコンテンツをバランスよくレイアウトしてください。
コンテンツ配置は基本12分割になります。がデザインによっては、多少逸脱してもかまいません。
bootstrap4、12分割グリッドの基準のPSDも資料として添付しております。
ご参考になさってください。

本分のフォントはゴシック系は游ゴシック、メイリオ、明朝系は遊明朝でお願いします。
飾り文字はフリーフォントか、googleフォントを利用してください。

メイン画像部分・グローバルメニューは、ワイド適用でお願いします。

不明点、質問などありましたらメッセージ等でご連絡ください。
サイトURL
ページ数
1ページ
希望イメージ
シンプル 複雑
単色 カラフル
暗い 明るい
日常 高級
遊び心 厳粛
未来的 伝統的
女性的 男性的
希望する色
青系、水色系
納品ファイル
• 高解像度JPG (.jpg)
• フォトショップ形式 (.psd)
補足説明
・資料上はサイト名(社名)や住所などは伏字にしております。
ご提案時点ではそのまま作成をお願いします。

・使用画像は当選後こちらで用意します。
ご提案時点では前項同様に、カンプデータ等をご使用のうえ、当選後に本内容へ差し替え修正をお願いします。
また、雰囲気が合っていれば、指定外の画像を追加掲載いただいてOKです。

・当選前提となった方は正式な社名及び連絡先をお伝えしますので修正対応をお願いします。
また希望の際は、当選後、中ページの制作及びコーディングも別途ご依頼可能です。

```html
<!DOCTYPE html>
<html lang="ja">
<head>
<meta charset="utf-8">
<title>木工架装施工専門業者</title>
<link href="https://fonts.googleapis.com/css2?family=Noto+Sans+JP:wght@400;500;700&family=Noto+Serif+JP:wght@500;700&family=Oswald:wght@500;700&display=swap" rel="stylesheet">
<style>
:root{
  --navy:#1d2c57;
  --navy-dark:#14203f;
  --ink:#333;
  --muted:#666;
  --beige:#f3ede3;
  --wood-light:#d9a26a;
  --wood-mid:#b8743c;
  --wood-dark:#7a4a26;
  --white:#fff;
  --line:#c9c9c9;
}
*{margin:0;padding:0;box-sizing:border-box}
html,body{width:1200px;height:2512px;overflow:hidden}
body{font-family:"Noto Sans JP",sans-serif;color:var(--ink);background:var(--white);position:relative}
.photo{position:absolute;display:block}
.ghost{position:absolute;font-family:"Oswald",sans-serif;font-weight:700;color:rgba(255,255,255,.35);letter-spacing:2px;white-space:nowrap;line-height:1}
.ghost.dark{color:rgba(120,110,100,.12)}
.btn{display:inline-flex;align-items:center;justify-content:center;gap:10px;background:var(--navy);color:var(--white);font-size:13px;font-weight:500;text-decoration:none}
.btn svg{width:12px;height:12px}

/* header */
.site-header{position:absolute;top:0;left:0;width:1200px;height:60px;background:var(--white);display:flex;align-items:center;padding:0 28px;z-index:3}
.brand{font-size:11px;line-height:1.5;color:var(--ink)}
.brand strong{display:block;font-size:16px;letter-spacing:3px;font-weight:500}
.global-nav{margin-left:auto;display:flex;align-items:center;gap:0}
.global-nav a{font-size:12px;color:var(--ink);text-decoration:none;padding:0 16px}
.global-nav a.current{background:var(--navy);color:#fff;padding:7px 16px}
.nav-contact{margin-left:20px;width:168px;height:38px}
.nav-tel{margin-left:10px;width:168px;height:38px;border:1px solid var(--navy);display:flex;align-items:center;justify-content:center;gap:8px;color:var(--navy);font-weight:700;font-size:15px}

/* hero */
.hero{position:absolute;top:0;left:0;width:1200px;height:560px;overflow:hidden}
.hero .photo{inset:0;width:100%;height:100%;background:linear-gradient(180deg,#4a4a4c 0%,#8b8780 18%,#c68a52 45%,#a8652f 75%,#6e4222 100%)}
.hero-copy{position:absolute;left:96px;top:370px;color:#fff}
.hero-copy h1{font-family:"Noto Serif JP",serif;font-size:34px;font-weight:700;letter-spacing:4px;margin-bottom:20px;text-shadow:0 2px 6px rgba(0,0,0,.3)}
.hero-copy p{font-family:"Noto Serif JP",serif;font-size:20px;letter-spacing:3px;line-height:1}
.hero-copy p span{display:inline-block;background:rgba(20,32,63,.75);padding:8px 10px;margin-bottom:6px}
.hero .ghost{left:0;top:488px;font-size:60px}

/* intro */
.intro{position:absolute;top:580px;left:0;width:1200px;height:400px}
.intro .photo{left:0;top:0;width:590px;height:380px;background:linear-gradient(160deg,#e8e6e2 0%,#b8b3ac 25%,#c07d43 55%,#8e5429 100%)}
.intro-body{position:absolute;left:640px;top:36px;width:500px}
.title-bar{border-left:4px solid var(--navy);padding-left:16px;font-size:22px;font-weight:700;color:var(--navy);line-height:1.55;letter-spacing:1px}
.intro-body p{font-size:12px;line-height:2;color:var(--muted);margin-top:22px}
.intro .ghost{left:250px;top:266px;font-size:58px;color:rgba(200,200,200,.55)}

/* business */
.business{position:absolute;top:1000px;left:0;width:1200px;height:400px;background:var(--beige)}
.business .photo{left:640px;top:0;width:560px;height:360px;background:linear-gradient(150deg,#3b3b3c 0%,#7b6a5a 20%,#cf8a48 50%,#a65f2c 85%)}
.sec-head h2{font-size:20px;font-weight:700;color:var(--navy);letter-spacing:2px}
.sec-head small{display:block;font-family:"Oswald",sans-serif;font-size:10px;color:var(--wood-mid);letter-spacing:2px;margin-top:4px}
.business-body{position:absolute;left:262px;top:72px;width:310px}
.business-body p{font-size:11px;line-height:2;color:var(--muted);margin:20px 0 26px}
.business-body .btn{width:132px;height:40px}
.business .ghost{left:20px;top:312px;font-size:64px}

/* works */
.works{position:absolute;top:1440px;left:0;width:1200px;height:440px}
.works .sec-head{text-align:center}
.works-grid{position:absolute;top:100px;left:0;width:1200px;display:flex;gap:10px;justify-content:center}
.works-grid .photo{position:static;width:292px;height:210px}
.w1{background:linear-gradient(160deg,#b9b6b0,#c7864a 55%,#8e522a)}
.w2{background:linear-gradient(160deg,#d8d6d2,#b86f36 50%,#8a4d25)}
.w3{background:linear-gradient(160deg,#efefed,#d09258 45%,#9c5b2c)}
.w4{background:linear-gradient(160deg,#c9c7c3,#c47b3e 50%,#7e4620)}
.works .btn{position:absolute;left:498px;top:350px;width:204px;height:42px}

/* contact */
.contact{position:absolute;top:1900px;left:0;width:1200px;height:380px;background:var(--beige)}
.contact .photo{left:0;top:0;width:560px;height:380px;background:linear-gradient(135deg,#6a6561 0%,#a79c90 35%,#c89a6c 65%,#8a6a4c 100%)}
.contact-body{position:absolute;left:662px;top:56px;width:360px}
.contact-body p{font-size:11px;line-height:2;color:var(--muted);margin:18px 0 16px}
.tel-box{width:248px;height:46px;border:1px solid var(--navy);background:#fff;display:flex;align-items:center;justify-content:center;gap:10px;color:var(--navy);font-weight:700;font-size:20px}
.contact-body .btn{width:248px;height:44px;margin-top:10px}
.contact .ghost{left:840px;top:316px;font-size:64px;color:rgba(170,160,150,.25)}

/* footer */
.site-footer{position:absolute;top:2280px;left:0;width:1200px;height:232px;background:linear-gradient(180deg,#8a5128 0%,#a8652f 30%,#7b4522 60%,#9b5c2c 100%);color:#fff}
.to-top{position:absolute;left:588px;top:-14px;width:26px;height:26px;border-radius:50%;background:var(--navy);display:flex;align-items:center;justify-content:center}
.footer-brand{position:absolute;left:262px;top:38px;font-size:10px;line-height:1.5}
.footer-brand strong{display:block;font-size:15px;letter-spacing:3px;font-weight:500}
.footer-info{position:absolute;left:262px;top:96px;font-size:10px;line-height:1.9}
.footer-nav{position:absolute;left:600px;top:40px;display:flex;gap:22px}
.footer-nav a{font-size:11px;color:#fff;text-decoration:none}
.footer-cta{position:absolute;left:860px;top:96px;width:80px;height:28px;border:1px solid rgba(255,255,255,.8);font-size:10px;display:flex;align-items:center;justify-content:center}
.copyright{position:absolute;left:0;bottom:0;width:100%;height:34px;background:rgba(20,32,63,.85);font-size:10px;display:flex;align-items:center;justify-content:center;letter-spacing:1px}
</style>
</head>
<body>

<section class="hero">
  <div class="photo" role="img" aria-label="木製フロアを施工した車両荷室の写真"></div>
  <div class="hero-copy">
    <h1>木工架装施工専門業者○○○○</h1>
    <p><span>きめ細かいこだわりと</span><br><span>お客様のご要望を叶える確かな技術</span></p>
  </div>
  <div class="ghost">KIRITANI WOODWORKING</div>
</section>

<header class="site-header">
  <div class="brand">自動車内装木工架装施工専門業者<strong>○○○○</strong></div>
  <nav class="global-nav">
    <a class="current" href="#">HOME</a>
    <a href="#">業務内容</a>
    <a href="#">施工事例</a>
    <a href="#">会社概要</a>
    <a class="btn nav-contact" href="#"><svg viewBox="0 0 12 12"><rect x="1" y="2.5" width="10" height="7" fill="none" stroke="#fff"/><path d="M1 2.5l5 4 5-4" fill="none" stroke="#fff"/></svg>お問い合わせ</a>
    <div class="nav-tel"><svg width="14" height="14" viewBox="0 0 24 24"><path d="M6.6 10.8a15 15 0 006.6 6.6l2.2-2.2a1 1 0 011-.25 11.4 11.4 0 003.6.6 1 1 0 011 1V20a1 1 0 01-1 1A17 17 0 013 4a1 1 0 011-1h3.5a1 1 0 011 1 11.4 11.4 0 00.6 3.6 1 1 0 01-.25 1z" fill="#1d2c57"/></svg>000-000-0000</div>
  </nav>
</header>

<section class="intro">
  <div class="photo" role="img" aria-label="木製フロアを敷いたバン荷室の写真"></div>
  <div class="intro-body">
    <h2 class="title-bar">車内の木工架装工事なら<br>○○○○にご相談ください！</h2>
    <p>"安心・確実"の架装施工を目指し、車内の木工架装を承っております。</p>
    <p>各種車両の荷室に合わせて、床板や棚などを一台ずつ丁寧に仕上げます。用途やご予算に合わせた最適なご提案が可能です。<br>リース車両や社用車の架装も多数の実績がございます。<br>まずはお気軽にご相談ください。</p>
  </div>
  <div class="ghost">WOODWORK FOR THE CAR</div>
</section>

<section class="business">
  <div class="business-body">
    <div class="sec-head"><h2>業務内容</h2><small>BUSINESS</small></div>
    <p>車内の床張りや棚の製作など、荷室の木工架装を中心に幅広く対応しております。<br>素材選びから施工まで一貫して行い、長く使える仕上がりをお届けします。</p>
    <a class="btn" href="#">業務内容へ<svg viewBox="0 0 12 12"><path d="M4 2l4 4-4 4" fill="none" stroke="#fff" stroke-width="1.5"/></svg></a>
  </div>
  <div class="photo" role="img" aria-label="荷室に施工した木製床板の写真"></div>
  <div class="ghost">BUSINESS</div>
</section>

<section class="works">
  <div class="sec-head"><h2>施工事例</h2><small>WORKS</small></div>
  <div class="works-grid">
    <div class="photo w1" role="img" aria-label="施工事例：荷室の木製フロア"></div>
    <div class="photo w2" role="img" aria-label="施工事例：後部から見た木製床"></div>
    <div class="photo w3" role="img" aria-label="施工事例：明るい荷室の床張り"></div>
    <div class="photo w4" role="img" aria-label="施工事例：側面からの木工架装"></div>
  </div>
  <a class="btn" href="#">すべて見る<svg viewBox="0 0 12 12"><path d="M4 2l4 4-4 4" fill="none" stroke="#fff" stroke-width="1.5"/></svg></a>
</section>

<section class="contact">
  <div class="photo" role="img" aria-label="木材をかんなで削る職人の手元の写真"></div>
  <div class="contact-body">
    <div class="sec-head"><h2>お問い合わせ</h2><small>CONTACT</small></div>
    <p>ご相談、ご質問などお気軽にお問い合わせください。</p>
    <div class="tel-box"><svg width="18" height="18" viewBox="0 0 24 24"><path d="M6.6 10.8a15 15 0 006.6 6.6l2.2-2.2a1 1 0 011-.25 11.4 11.4 0 003.6.6 1 1 0 011 1V20a1 1 0 01-1 1A17 17 0 013 4a1 1 0 011-1h3.5a1 1 0 011 1 11.4 11.4 0 00.6 3.6 1 1 0 01-.25 1z" fill="#1d2c57"/></svg>000-000-0000</div>
    <a class="btn" href="#"><svg viewBox="0 0 12 12"><rect x="1" y="2.5" width="10" height="7" fill="none" stroke="#fff"/><path d="M1 2.5l5 4 5-4" fill="none" stroke="#fff"/></svg>お問い合わせ</a>
  </div>
  <div class="ghost">CONTACT</div>
</section>

<footer class="site-footer">
  <a class="to-top" href="#" aria-label="ページトップへ"><svg width="10" height="10" viewBox="0 0 12 12"><path d="M2 8l4-4 4 4" fill="none" stroke="#fff" stroke-width="1.5"/></svg></a>
  <div class="footer-brand">自動車内装木工架装施工専門業者<strong>○○○○</strong></div>
  <div class="footer-info">〒000-0000 ○○県○○市○○町0-0-0<br>TEL：000-000-0000 ／ FAX：000-000-0000</div>
  <nav class="footer-nav">
    <a href="#">HOME</a><a href="#">業務内容</a><a href="#">施工事例</a><a href="#">会社概要</a><a href="#">お問い合わせ</a>
  </nav>
  <div class="footer-cta">TOP</div>
  <div class="copyright">© ○○○○ All Rights Reserved.</div>
</footer>

</body>
</html>
```